Perky professional Bookkeeping Business card design needed

I need a business card for my new bookkeeping business. My target market is the owners of small businesses. I am a bright and bubbly young lady, not your typical accountant type and am looking for a bright, modern, perky yet professional card to reflect this.
I would like to use the symbol from framevault http://www.framevault.com/cat.mhtml?searchterm=business+wizard&search_group=&lang=en&search_source=search_form#id=60384915
as my logo but am open to colour schemes.
I want the design of the card to create confidence but not be too formal. Most people are scared of their bookkeepers/accountants and I want to be seen as approachable.
Target Market(s)
Business owners
Industry/Entity Type
Business
Contact Information for Business Card
Tally Spark Bookkeeping - image and name
Maren Holloway BBUS
Registered BAS AGENT 51730628
PO Box 738
Glen Harrow VIC 3981
Ph: 0437682915
Email: maren@tallysparkbookkeeping.com.au
Web: www.tallysparkbookkeeping.com.au
Tag line: Acheiving Maximum Results (not sure whether to include)
Look and feel

```html
<!DOCTYPE html>
<html lang="en">
<head>
<meta charset="utf-8">
<title>Tally Spark Bookkeeping Business Card</title>
<link rel="stylesheet" href="https://fonts.googleapis.com/css2?family=Tinos:ital,wght@0,400;1,400&family=Ubuntu:wght@500&display=swap">
<style>
  :root {
    --page-bg: #d9d9d9;
    --card-brown-light: #5a4636;
    --card-brown: #3d2e23;
    --card-brown-dark: #2a201a;
    --band-black: #141414;
    --band-black-light: #262626;
    --divider: #8d8d8d;
    --logo-grey: #b9b3ad;
    --text-light: #e6e2de;
    --text-muted: #c9c2bb;
    --photo-top: #6b5848;
    --photo-mid: #8a7868;
    --photo-low: #4c4540;
  }
  * { margin: 0; padding: 0; box-sizing: border-box; }
  html, body {
    width: 1200px;
    height: 861px;
    overflow: hidden;
    background: var(--page-bg);
  }
  .canvas {
    position: relative;
    width: 1200px;
    height: 861px;
  }
  .business-card {
    position: absolute;
    left: 150px;
    top: 173px;
    width: 900px;
    height: 514px;
    overflow: hidden;
    background: var(--band-black);
    box-shadow: 0 10px 30px rgba(0, 0, 0, 0.35);
  }
  .card-top {
    position: absolute;
    left: 0;
    top: 0;
    width: 100%;
    height: 308px;
    background: radial-gradient(ellipse at 35% 25%, var(--card-brown-light) 0%, var(--card-brown) 55%, var(--card-brown-dark) 100%);
  }
  .divider {
    position: absolute;
    left: 0;
    top: 308px;
    width: 100%;
    height: 8px;
    background: linear-gradient(180deg, var(--divider), #4a4a4a);
  }
  .card-bottom {
    position: absolute;
    left: 0;
    top: 316px;
    width: 100%;
    height: 198px;
    background: linear-gradient(180deg, var(--band-black-light), var(--band-black));
  }
  .brand {
    position: absolute;
    left: 44px;
    top: 34px;
    display: flex;
    align-items: center;
    gap: 20px;
  }
  .brand-mark {
    width: 104px;
    height: 104px;
    border-radius: 50%;
    border: 5px solid var(--logo-grey);
  }
  .brand-name {
    font-family: "Ubuntu", sans-serif;
    font-weight: 500;
    font-size: 38px;
    line-height: 1.1;
    color: var(--logo-grey);
  }
  .tagline {
    position: absolute;
    left: 168px;
    top: 132px;
    font-family: "Tinos", serif;
    font-style: italic;
    font-size: 15px;
    color: var(--text-muted);
    opacity: 0.75;
  }
  .agent-name {
    position: absolute;
    left: 40px;
    top: 178px;
    font-family: "Tinos", serif;
    font-weight: 400;
    font-size: 50px;
    line-height: 1.2;
    color: var(--text-light);
  }
  .credentials {
    position: absolute;
    left: 42px;
    top: 244px;
    font-family: "Tinos", serif;
    font-size: 21px;
    line-height: 1.2;
    color: var(--text-muted);
  }
  .contact-list {
    position: absolute;
    left: 40px;
    top: 338px;
    list-style: none;
    font-family: "Tinos", serif;
    font-size: 20px;
    line-height: 32px;
    color: var(--text-light);
  }
  .portrait {
    position: absolute;
    left: 600px;
    top: 40px;
    width: 270px;
    height: 474px;
    border-radius: 110px 110px 0 0;
    background: linear-gradient(180deg, var(--photo-top) 0%, var(--photo-mid) 35%, var(--photo-low) 100%);
  }
</style>
</head>
<body>
<main class="canvas">
  <section class="business-card">
    <div class="card-top"></div>
    <div class="divider"></div>
    <div class="card-bottom"></div>

    <div class="brand">
      <div class="brand-mark"></div>
      <div class="brand-name">Tally Spark<br>Bookkeeping</div>
    </div>
    <p class="tagline">Delivering Steady Growth</p>

    <h1 class="agent-name">Maren Holloway</h1>
    <p class="credentials">BBUS Registered<br>BAS Agent 51730628</p>

    <ul class="contact-list">
      <li>Address: PO Box 738 Glen Harrow VIC 3981</li>
      <li>Phone: 0437682915</li>
      <li>Email: maren@tallysparkbookkeeping.com.au</li>
      <li>Web: www.tallysparkbookkeeping.com.au</li>
    </ul>

    <div class="portrait" role="img" aria-label="Portrait photo of a smiling businesswoman in a grey suit with arms folded"></div>
  </section>
</main>
</body>
</html>
```